Website Refresh Needed - Large Couples Therapy Group

We are a large couples counselling group in Australia, and we have some key pages of our website that need refreshing, as it's a few years old now.
Similar colour palette as currently, and the same colours as the logo. No new logo required.
Total of 7 new (updated) page templates designs are needed:
1. HOME: https://www.velmoraclinic.com.au/
2: CONTACT US: https://www.velmoraclinic.com.au/contact/
3: RC CITY PAGE: https://www.velmoraclinic.com.au/city/sydney/
4: ST CITY PAGE: https://www.velmoraclinic.com.au/our-counselling/sex-therapy/sex-therapy-sydney/
5: ALL BLOGS: https://www.velmoraclinic.com.au/blog/
6: BLOG: https://www.velmoraclinic.com.au/sexual-desires-in-men-and-women-what-are-the-real-differences/
7: MAIN STANDARD PAGE: https://www.velmoraclinic.com.au/our-counselling/couples-relationship-counselling/

Target Market(s)

couples who are going through a crisis in their relationship or marriage.

Number of Pages Required

5+ page

Colors
86cfc6
b8a6cd
cfdfed

Requirements
Must have
• Calm, reassuring colours. People are stressed and need to know we can help.
Should not have
• No bright oranges or yellows.

```html
<!DOCTYPE html>
<html lang="en">
<head>
<meta charset="utf-8">
<title>Velmora Clinic – Relationship &amp; Marriage Counselling</title>
<link href="https://fonts.googleapis.com/css2?family=Roboto:wght@300;400;500;700&family=Raleway:wght@400;500&display=swap" rel="stylesheet">
<style>
:root{
  --teal:#0f7f8b;
  --teal-dark:#0b6f7a;
  --mint:#86cfc6;
  --grey-bg:#eeeff1;
  --ink:#2b2b2b;
  --ink-soft:#4a4a4a;
  --white:#ffffff;
  --line:#d6d9dc;
}
*{box-sizing:border-box;margin:0;padding:0}
html,body{width:1200px;height:2864px;overflow:hidden}
body{font-family:'Roboto',sans-serif;color:var(--ink);background:var(--white);position:relative}
.section{position:absolute;left:0;width:1200px}
.wrap{position:relative;width:900px;margin:0 auto;height:100%}
.btn{display:inline-flex;align-items:center;justify-content:center;background:var(--teal);color:var(--white);font-weight:700;text-transform:uppercase;text-decoration:none;border-radius:2px}

/* header */
.site-header{top:0;height:128px;background:var(--white);border-bottom:1px solid var(--line)}
.call{position:absolute;left:150px;top:58px;font-size:13px;color:var(--ink-soft)}
.call strong{font-size:18px;color:var(--ink);font-weight:500}
.brand{position:absolute;left:465px;top:22px;display:flex;align-items:center;gap:12px;text-decoration:none}
.brand-dot{width:34px;height:34px;border-radius:50%;background:var(--teal)}
.brand-name{font-size:36px;font-weight:300;color:var(--teal);letter-spacing:.5px}
.header-cta{position:absolute;left:885px;top:47px;width:165px;height:30px;font-size:10px;font-weight:500}
.main-nav{position:absolute;left:0;width:1200px;top:102px;display:flex;justify-content:center;gap:36px;font-size:11px;font-weight:700}
.main-nav a{color:var(--ink);text-decoration:none}

/* hero */
.hero{top:128px;height:392px;background:linear-gradient(180deg,#5e6f80 0%,#8c8f93 35%,#b9a99a 60%,#7d8b98 80%,#5c6c7c 100%)}
.hero-copy{position:absolute;left:140px;top:122px;width:410px;text-align:right;color:var(--white)}
.hero-copy h1{font-size:42px;font-weight:700;line-height:50px}
.hero-copy p{font-size:18px;font-weight:300;line-height:22px;margin-top:10px}
.hero-btn{position:absolute;left:367px;top:283px;width:149px;height:34px;font-size:13px;font-weight:500}

/* search */
.finder{top:520px;height:60px;background:var(--mint)}
.finder h2{position:absolute;left:198px;top:19px;font-size:18px;font-weight:500;color:#1f3b3b}
.select{position:absolute;top:11px;height:38px;background:var(--white);border:1px solid #cfd6d6;border-radius:2px;font-size:11px;color:#777;display:flex;align-items:center;padding:0 22px;justify-content:space-between}
.select svg{width:16px;height:10px}
.sel-type{left:494px;width:240px}
.sel-loc{left:749px;width:181px}
.finder .btn{position:absolute;left:944px;top:11px;width:106px;height:38px;font-size:11px}

/* welcome */
.welcome{top:580px;height:487px;background:var(--grey-bg)}
.welcome-photo{position:absolute;left:150px;top:16px;width:225px;height:224px;background:linear-gradient(160deg,#a7adb4,#5f666e);border:1px solid #c9ccd0}
.welcome-body{position:absolute;left:400px;top:20px;width:650px}
.welcome h2{font-size:19px;font-weight:500;margin-bottom:16px}
.welcome p{font-size:11.5px;line-height:16px;color:var(--ink-soft);margin-bottom:15px}
.welcome p.lead{font-weight:700;color:var(--ink)}
.welcome-rest{position:absolute;left:150px;top:256px;width:900px}

/* help */
.help-head{top:1067px;height:75px;text-align:center}
.help-head h2{font-size:22px;font-weight:500;margin-top:17px}
.help-head p{font-size:10.5px;letter-spacing:1px;margin-top:10px;color:var(--ink)}
.services{top:1142px;height:364px;background:var(--grey-bg)}
.service{position:absolute;top:11px;width:199px;text-align:center}
.service-img{width:199px;height:188px;border:1px solid #cfd3d6}
.service h3{font-size:14px;font-weight:400;margin-top:26px;line-height:17px;height:34px}
.service p{font-family:'Raleway',sans-serif;font-size:10px;line-height:12px;color:#555;text-align:left;padding:0 9px;margin-top:4px;height:50px}
.service .btn{width:135px;height:29px;font-size:9.5px;margin-top:6px}

/* topics */
.topics-head{top:1506px;height:63px;text-align:center}
.topics-head h2{font-size:22px;font-weight:500;margin-top:18px}
.topics{top:1569px;height:181px;background:var(--grey-bg)}
.topic-col{position:absolute;top:26px;list-style:none}
.topic-col li{font-size:12px;line-height:28px;color:var(--ink-soft);padding-left:14px;position:relative}
.topic-col li::before{content:"";position:absolute;left:0;top:12px;width:5px;height:5px;border-radius:50%;background:var(--ink)}

/* testimonial */
.words-head{top:1750px;height:61px;text-align:center}
.words-head h2{font-size:22px;font-weight:500;margin-top:17px}
.testimonial{top:1811px;height:448px;background:linear-gradient(90deg,#b9bfbc 0%,#cfd1ce 35%,#c5b2a8 62%,#b98677 78%,#c7a7a4 100%)}
.quote{position:absolute;left:220px;top:110px;width:420px;font-size:15.5px;line-height:27px;font-weight:300;color:#3a3a3a}
.quote-mark{position:absolute;font-size:48px;font-weight:700;color:var(--teal);line-height:1}
.quote cite{display:block;text-align:right;padding-right:50px;font-style:normal;font-size:13px;font-weight:400;color:var(--teal);line-height:18px}

/* blogs */
.blogs-head{top:2259px;height:65px;text-align:center}
.blogs-head h2{font-size:22px;font-weight:500;margin-top:17px}
.blogs{top:2324px;height:312px;background:var(--grey-bg)}
.post{position:absolute;top:16px;width:270px}
.post-img{width:270px;height:150px}
.post h3{font-size:13px;font-weight:400;line-height:16px;margin-top:19px;color:var(--ink)}
.post a{font-size:11.5px;color:var(--teal);text-decoration:none;line-height:17px}
.post time{display:block;font-size:8px;color:#777;margin-top:3px}
.blogs .btn{position:absolute;left:532px;top:267px;width:135px;height:28px;font-size:9.5px}

/* footer */
.site-footer{top:2636px;height:228px;background:var(--mint);text-align:center}
.footer-brand{position:absolute;left:490px;top:38px;display:flex;align-items:center;gap:12px}
.footer-brand .brand-name{font-size:34px}
.footer-nav{position:absolute;left:0;width:1200px;top:108px;display:flex;justify-content:center;gap:17px;font-size:11px;font-weight:700}
.footer-nav a{color:#1f3b3b;text-decoration:none}
.footer-nav span{color:#1f3b3b;font-weight:400}
.social{position:absolute;left:568px;top:144px;display:flex;gap:22px}
.social a{width:22px;height:22px;border-radius:50%;background:var(--teal);display:block}
.copyright{position:absolute;left:0;width:1200px;top:180px;font-size:10px;color:#2f4a4a}
</style>
</head>
<body>

<header class="section site-header">
  <div class="call">Call Us Now <strong>1300 555 019</strong></div>
  <a class="brand" href="https://www.velmoraclinic.com.au/"><span class="brand-dot"></span><span class="brand-name">Velmora Clinic</span></a>
  <a class="btn header-cta" href="https://www.velmoraclinic.com.au/contact/">Request an Appointment</a>
  <nav class="main-nav">
    <a href="https://www.velmoraclinic.com.au/">Home</a>
    <a href="#">Counselling Types</a>
    <a href="https://www.velmoraclinic.com.au/city/sydney/">Relationship Counselling Locations</a>
    <a href="https://www.velmoraclinic.com.au/our-counselling/sex-therapy/sex-therapy-sydney/">Sex Therapy Locations</a>
    <a href="#">Quizzes</a>
    <a href="#">Fees &amp; Rebets</a>
    <a href="https://www.velmoraclinic.com.au/contact/">Contact Us</a>
  </nav>
</header>

<section class="section hero" role="img" aria-label="Couple silhouetted on a swing above calm sea water at sunset">
  <div class="hero-copy">
    <h1>Expert Relationship &amp; Marriage Counselling</h1>
    <p>Start a Relationship with an<br>Exceptional&nbsp; Counselor</p>
  </div>
  <a class="btn hero-btn" href="#">Get Involved</a>
</section>

<section class="section finder">
  <h2>Search Our Therapist Near You</h2>
  <div class="select sel-type">Select Type of Your Counselling <svg viewBox="0 0 16 10"><path d="M1 1l7 7 7-7" fill="none" stroke="#333" stroke-width="2"/></svg></div>
  <div class="select sel-loc">Location or Postcode <svg viewBox="0 0 16 10"><path d="M1 1l7 7 7-7" fill="none" stroke="#333" stroke-width="2"/></svg></div>
  <a class="btn" href="#">Search</a>
</section>

<section class="section welcome">
  <div class="welcome-photo" role="img" aria-label="Portrait of the clinic founder in a dark suit with arms folded"></div>
  <div class="welcome-body">
    <h2>Welcome to the Velmora Clinic....</h2>
    <p>You've come to the right place if you value your relationship, (along with being true to yourself) and would like help with how to repair the inevitable difficulties that come up in most relationships, and build a stronger more authentic connection.</p>
    <p>None of us, when we fall in love, imagine how difficult our relationship is going to be at times. We always hope for the best, then do our best, and still we can find that we can get stranded in problems that we don't really understand. We can unwittingly get into distressing lose-lose negative cycles, and not know how to get out of them.</p>
    <p>This is perfectly understandable because most of us haven't been taught how to have a great relationship. We're just doing the best we know how.</p>
    <p class="lead">There is a very complex blend of science and art in creating great relationships, and this is both our passion and</p>
  </div>
  <div class="welcome-rest">
    <p>We're a group of nearly 100 psychologists, counsellors and sex therapists Australia wide who are passionate about relationships; understanding what makes them tick, how to best overcome difficulties, how to communicate effectively, how to get your relationship back on track, and even build new depths of compassion, understanding and honesty.</p>
    <p>We can give you the insight into the patterns you may inadvertently find yourself in that have caused hurt and confusion for you, and help you discover what's stopping you from having the relationship you'd love, so you can start taking steps towards the relationship that you want, creating an emotional safe haven for each other and a more authentic intimacy.</p>
    <p>I welcome you to begin your journey back to a finding the full relationship potential of you as a couple.</p>
    <p class="lead">"At the end of our life what matters most is how well we loved"</p>
    <p>Warmly,</p>
    <p class="lead">Maren Velmore</p>
  </div>
</section>

<section class="section help-head">
  <h2>Do You Need Help With</h2>
  <p>IF YOU JUST NEED TO BE HEARD, WE ARE HERE TO LISTEN.</p>
</section>

<section class="section services">
  <article class="service" style="left:150px">
    <div class="service-img" role="img" aria-label="Couple talking with a counsellor" style="background:linear-gradient(135deg,#d9dcdc,#a9a39a)"></div>
    <h3>Relationship Counselling</h3>
    <p>Communication, recovering from an affair, loss of intimacy and love or power battles?</p>
    <a class="btn" href="https://www.velmoraclinic.com.au/our-counselling/couples-relationship-counselling/">Find Out More</a>
  </article>
  <article class="service" style="left:383px">
    <div class="service-img" role="img" aria-label="Two pairs of feet on white bed sheets" style="background:linear-gradient(135deg,#e4e6ea,#b29a88)"></div>
    <h3>Sex Therapy Counselling</h3>
    <p>Low sexual drive, erectile difficulties, premature ejaculation, differing libidos or porn addiction?</p>
    <a class="btn" href="https://www.velmoraclinic.com.au/our-counselling/sex-therapy/sex-therapy-sydney/">Find Out More</a>
  </article>
  <article class="service" style="left:617px">
    <div class="service-img" role="img" aria-label="Clenched fist against cracked glass" style="background:linear-gradient(135deg,#c9dedd,#b99c86)"></div>
    <h3>Anger Management Counselling</h3>
    <p>Managing irrational outbursts, while learning to express your anger in healthy ways?</p>
    <a class="btn" href="#">Find Out More</a>
  </article>
  <article class="service" style="left:851px">
    <div class="service-img" role="img" aria-label="Silhouette facing a crowned reflection in a mirror frame at dusk" style="background:linear-gradient(180deg,#4f7aa8,#c9a06a 75%,#2b2b2b)"></div>
    <h3 style="margin-top:22px">Narcissism Counselling</h3>
    <p>Managing narcissistic, superior, entitled, arrogant behaviour or lack of empathy?</p>
    <a class="btn" href="#">Find Out More</a>
  </article>
</section>

<section class="section topics-head"><h2>Our Relationship Therapists Topics</h2></section>

<section class="section topics">
  <ul class="topic-col" style="left:203px">
    <li>Affairs</li><li>Controlling behaviour</li><li>Verbal abuse</li><li>Lack of intimacy</li><li>Imbalance of power</li>
  </ul>
  <ul class="topic-col" style="left:482px">
    <li>Poor communication</li><li>Loss of love</li><li>Relationship neglect</li><li>Sexual problems</li><li>Problems from childhood</li>
  </ul>
  <ul class="topic-col" style="left:783px">
    <li>Problems with parenting your children</li><li>Step children and in-laws</li><li>Verbal abuse</li><li>All forms of family problems</li><li>Anger management problems</li>
  </ul>
</section>

<section class="section words-head"><h2>In Thier Own Words</h2></section>

<section class="section testimonial" role="img" aria-label="Smiling client in a coral top sitting at a laptop in a bright office">
  <span class="quote-mark" style="left:190px;top:105px">“</span>
  <blockquote class="quote">
    Velmora helped me realize that I do believe people can change. I'm not the person I was three months ago, broken and fearful. I'm healthy and happy and for the first time being kind to myself. Thank you for giving me my life back.
    <cite>- Client Testimonial</cite>
  </blockquote>
  <span class="quote-mark" style="left:614px;top:210px">”</span>
</section>

<section class="section blogs-head"><h2>Latest Blogs</h2></section>

<section class="section blogs">
  <article class="post" style="left:150px">
    <div class="post-img" role="img" aria-label="Distressed woman holding her head with a man in the background" style="background:linear-gradient(90deg,#e9e7e2,#d3cfc8 60%,#b7b6b6)"></div>
    <h3>What is Borderline Personality Disorder and how does it affect my relationship?</h3>
    <a href="https://www.velmoraclinic.com.au/blog/">Learn more</a>
    <time>On 24 June 2020</time>
  </article>
  <article class="post" style="left:465px">
    <div class="post-img" role="img" aria-label="Smiling couple lying under a white sheet" style="background:linear-gradient(90deg,#c9925f,#e6d6c8 55%,#a77c60)"></div>
    <h3>Sexual Desires in Men and Women; What Are the Real Differences?</h3>
    <a href="https://www.velmoraclinic.com.au/sexual-desires-in-men-and-women-what-are-the-real-differences/">Learn more</a>
    <time>On 05 May 2020</time>
  </article>
  <article class="post" style="left:780px">
    <div class="post-img" role="img" aria-label="Couple lying together on a picnic blanket in the grass" style="background:linear-gradient(135deg,#b8aaa9,#8f8174 60%,#c3b59c)"></div>
    <h3>6 Steps To Becoming An Emotionally Available Lover</h3>
    <a href="https://www.velmoraclinic.com.au/blog/">Learn more</a>
    <time>On 28 April 2020</time>
  </article>
  <a class="btn" href="https://www.velmoraclinic.com.au/blog/">More Articles</a>
</section>

<footer class="section site-footer">
  <div class="footer-brand"><span class="brand-dot"></span><span class="brand-name">Velmora Clinic</span></div>
  <nav class="footer-nav">
    <a href="https://www.velmoraclinic.com.au/">Home</a><span>|</span>
    <a href="#">About Us</a><span>|</span>
    <a href="#">Members Log In</a><span>|</span>
    <a href="https://www.velmoraclinic.com.au/blog/">Our Blogs</a><span>|</span>
    <a href="https://www.velmoraclinic.com.au/contact/">Contact Us</a><span>|</span>
    <a href="#">FAQ`s</a>
  </nav>
  <div class="social">
    <a href="#" aria-label="Social profile one"></a>
    <a href="#" aria-label="Social profile two"></a>
    <a href="#" aria-label="Social profile three"></a>
  </div>
  <p class="copyright">© 2020 Velmora Clinic. All rights reserved.</p>
</footer>

</body>
</html>
```